OTT TV and VOD Service Website (like Vexamo.tv ; Brindo etc.)

Site will be used as a marketing page integrated with subscription processing (Quellpay). Looking for someone with solid experience in designing video content driven sites. For the looks; clean, modern, black background with rich "popping" VOD and live TV channel titles.

Target Market(s)

Video-on-demand and international live TV channel subscribers in Asia

Coding

Number of Pages Required

Font styles to use
Other font styles liked:

Requirements
Must have
• Start with an awesome looking "coming soon" page, featuring a logo on black background with video (i.e. a movie trailers) playing in the background. This page should also have an understated "about" link and an email "contact" form.
Site: Scrollable interfaces: Service / Live Channels / VOD / Subscribe.
Contrasting backgrounds as the page is being scrolled. Black as a dominating background color. See Vexamo.tv site for inspiration
There will be contact form (Register)
Nice to have
• Dynamic video background on the home page (trailer / title / channel promo)
Clear interface separation between live TV channels and VOD
Should not have
• Typical template looking scrolling site with boring icons and

```html
<!DOCTYPE html>
<html lang="en">
<head>
<meta charset="utf-8">
<title>Lumora.tv — Watch Anytime</title>
<link rel="stylesheet" href="https://fonts.googleapis.com/css2?family=Ubuntu:wght@500;700&family=Roboto:wght@400;500;700&display=swap">
<style>
:root{
  --black:#000;
  --ink:#111;
  --muted:#555;
  --white:#fff;
  --blue:#1f95e3;
  --green:#84c03a;
  --grad:linear-gradient(90deg,var(--blue),var(--green));
  --soft:#f2f2f2;
  --footer:#1b1b1b;
  --live:#e4121b;
  --field-line:#dcdcdc;
}
*{box-sizing:border-box;margin:0;padding:0}
html,body{width:1200px;height:2579px;overflow:hidden}
body{font-family:"Roboto",Arial,sans-serif;background:var(--white);color:var(--ink);position:relative}
a{text-decoration:none}
.abs{position:absolute}
.heading{font-family:"Ubuntu","Roboto",sans-serif;font-weight:700}

/* header */
.site-header{left:0;top:0;width:1200px;height:91px;background:var(--black)}
.brand{font-family:"Roboto",sans-serif;font-weight:500;color:var(--white);font-size:36px;left:111px;top:24px;letter-spacing:.3px}
.nav{top:25px;right:113px;display:flex;align-items:center;height:42px}
.nav a{font-weight:500;font-size:16px}
.nav .home{color:var(--blue);margin-right:28px;position:relative}
.nav .home::before{content:"";position:absolute;left:16px;top:-14px;border-left:12px solid #5fb98a;border-top:6px solid transparent;border-bottom:6px solid transparent}
.nav .about{color:var(--white);margin-right:26px}
.nav .search{margin-right:26px;display:flex}
.nav .touch{border:2px solid #4aa7a0;border-radius:22px;color:var(--blue);padding:9px 14px;margin-right:18px}
.nav .signin{background:var(--grad);color:var(--white);border-radius:22px;padding:11px 18px;display:flex;align-items:center;gap:6px}

/* hero */
.hero{left:0;top:91px;width:1200px;height:542px;background:
  radial-gradient(circle at 19% 6%,rgba(190,240,235,.55),transparent 18%),
  radial-gradient(ellipse 30% 40% at 30% 35%,rgba(110,170,180,.55),transparent 70%),
  radial-gradient(circle at 73% 38%,rgba(255,190,90,.45),transparent 3%),
  radial-gradient(circle at 95% 36%,rgba(255,170,70,.55),transparent 3.5%),
  radial-gradient(circle at 81% 66%,rgba(255,170,60,.5),transparent 2.5%),
  radial-gradient(ellipse 50% 60% at 85% 45%,rgba(40,60,30,.55),transparent 70%),
  linear-gradient(180deg,transparent 70%,rgba(10,40,40,.55)),
  linear-gradient(100deg,#1e4a57 0%,#2b6569 35%,#355f45 62%,#4b7a2e 85%,#5e8f2a 100%)}
.hero-title{left:0;width:1200px;top:263px;text-align:center;color:var(--white);font-size:44px}
.hero-copy{left:350px;width:500px;top:331px;text-align:center;color:var(--white);font-size:17px;line-height:27px;font-weight:500}
.btn-grad{background:var(--grad);color:var(--white);font-weight:700;border-radius:30px;display:flex;align-items:center;justify-content:center}
.watch{left:508px;top:410px;width:183px;height:53px;font-size:16px;gap:8px}
.follow{left:104px;top:252px;color:var(--white);font-size:14px;letter-spacing:1px;writing-mode:vertical-rl;transform:rotate(180deg)}
.follow-line{left:111px;top:342px;width:1px;height:50px;background:rgba(255,255,255,.7)}
.follow-icons{left:104px;top:408px;display:flex;flex-direction:column;gap:16px}
.follow-icons span{width:12px;height:12px;border-radius:2px;background:var(--white);display:block}

/* category grid */
.tile{overflow:hidden;color:var(--white)}
.tile .shade{position:absolute;inset:0;background:linear-gradient(180deg,transparent 45%,rgba(0,0,0,.6))}
.tile h3{position:absolute;left:17px;bottom:38px;font-size:19px;font-weight:700}
.tile p{position:absolute;left:17px;bottom:17px;font-size:14px}
.feature{left:0;top:647px;width:619px;height:459px;background:
  radial-gradient(ellipse 14% 18% at 42% 32%,rgba(240,110,40,.85),transparent 70%),
  radial-gradient(circle at 86% 49%,rgba(200,160,70,.9),transparent 7%),
  radial-gradient(ellipse 40% 20% at 60% 20%,rgba(255,255,255,.45),transparent 70%),
  linear-gradient(180deg,#2755c4 0%,#4b82d8 35%,#8fb3e4 52%,#3c5a8a 60%,#3f7b2e 68%,#2f6a1e 100%)}
.feature .live{position:absolute;right:19px;top:16px;background:var(--live);font-weight:700;font-size:14px;padding:3px 12px;border-radius:4px}
.feature h2{position:absolute;left:111px;top:350px;width:360px;font-size:18px;line-height:23px;font-weight:700}
.feature .date{position:absolute;left:111px;top:406px;font-size:15px;display:flex;align-items:center;gap:6px}
.t-movies{left:634px;top:647px;width:290px;height:221px;background:
  radial-gradient(ellipse 25% 40% at 22% 50%,rgba(150,70,50,.6),transparent 70%),
  radial-gradient(ellipse 40% 30% at 75% 25%,rgba(170,185,200,.55),transparent 70%),
  linear-gradient(135deg,#4d5660,#262a31 60%,#15181c)}
.t-seasons{left:939px;top:647px;width:261px;height:221px;background:
  radial-gradient(ellipse 30% 45% at 30% 40%,rgba(200,150,110,.7),transparent 70%),
  radial-gradient(ellipse 30% 45% at 62% 40%,rgba(215,170,130,.7),transparent 70%),
  linear-gradient(135deg,#9a8470,#5a4a3e 60%,#3c3129)}
.t-news{left:634px;top:884px;width:290px;height:222px;background:
  radial-gradient(ellipse 25% 45% at 35% 45%,rgba(220,200,185,.55),transparent 70%),
  radial-gradient(ellipse 50% 35% at 70% 25%,rgba(170,180,185,.5),transparent 70%),
  linear-gradient(135deg,#75797e,#3a3e43 60%,#22262a)}
.t-kids{left:939px;top:884px;width:261px;height:222px;background:
  radial-gradient(ellipse 24% 18% at 50% 0%,rgba(250,235,160,.95),transparent 90%),
  radial-gradient(ellipse 20% 30% at 52% 72%,rgba(255,160,40,.85),transparent 70%),
  linear-gradient(180deg,#1c3a42,#22443b 55%,#3d3a22 85%,#5a3c1a)}

/* promo */
.promo-title{left:111px;top:1208px;font-size:34px;line-height:36px;color:var(--ink)}
.promo-copy{left:111px;top:1298px;width:440px;font-size:15.5px;line-height:26px;color:var(--muted)}
.trial{left:111px;top:1406px;width:230px;height:52px;font-size:16px}
.phone{border:8px solid #f4f4f4;border-bottom:none;border-radius:26px 26px 0 0;box-shadow:0 0 12px rgba(0,0,0,.12);overflow:hidden}
.phone-left{left:667px;top:1278px;width:143px;height:277px;background:
  radial-gradient(circle at 30% 20%,rgba(190,200,90,.25),transparent 30%),
  radial-gradient(circle at 70% 70%,rgba(140,190,80,.2),transparent 35%),
  linear-gradient(180deg,#173a3c,#0e2a35)}
.phone-right{left:810px;top:1178px;width:220px;height:377px;background:
  radial-gradient(ellipse 22% 18% at 55% 45%,rgba(215,225,80,.8),transparent 70%),
  radial-gradient(ellipse 25% 25% at 50% 25%,rgba(190,130,95,.7),transparent 70%),
  radial-gradient(ellipse 18% 20% at 88% 42%,rgba(120,190,220,.6),transparent 70%),
  linear-gradient(180deg,#d3cdc1 0%,#b8a690 30%,#a37a58 55%,#7a3a1c 80%,#6a2512 100%)}
.notch{position:absolute;left:50%;top:0;transform:translateX(-50%);width:60%;height:14px;background:#f4f4f4;border-radius:0 0 10px 10px}
.phone-brand{position:absolute;left:0;width:127px;text-align:center;top:92px;color:#43b8c0;font-size:22px;font-weight:500}
.phone-login{position:absolute;left:34px;top:175px;width:74px;height:26px;border-radius:14px;background:var(--grad);color:var(--white);font-size:14px;font-weight:700;display:flex;align-items:center;justify-content:center}
.phone-caption{position:absolute;left:14px;top:305px;color:var(--white);font-size:14px;font-weight:700;line-height:23px}

/* contact */
.contact{left:0;top:1555px;width:1200px;height:467px;background:var(--soft)}
.contact-title{left:0;width:1200px;top:1610px;text-align:center;font-size:35px}
.contact-copy{left:0;width:1200px;top:1662px;text-align:center;font-size:15px;color:var(--muted)}
.field{background:var(--white);border:1px solid var(--field-line);display:flex;align-items:center;gap:8px;padding-left:16px;font-size:15px;color:#444}
.f-name{left:188px;top:1722px;width:399px;height:43px}
.f-phone{left:188px;top:1779px;width:399px;height:43px}
.f-email{left:188px;top:1836px;width:399px;height:43px}
.f-msg{left:612px;top:1722px;width:399px;height:157px;align-items:flex-start;padding-top:14px}
.submit{left:537px;top:1914px;width:127px;height:46px;font-size:16px}

/* bundle */
.bundle{left:0;top:2022px;width:1200px;height:194px;background:linear-gradient(90deg,#7bbd3c 0%,#39a69a 35%,#2a9bd2 70%,#1f95e3 100%)}
.partners{left:111px;top:2117px;display:flex;align-items:center;gap:20px;color:var(--white);font-weight:500;font-size:20px}
.bundle-kicker{left:456px;top:2073px;color:var(--white);font-weight:700;font-size:15px}
.bundle-line{left:456px;top:2097px;width:470px;color:var(--white);font-size:18px;white-space:nowrap}
.bundle-more{left:456px;top:2143px;color:var(--white);font-weight:700;font-size:15px;text-decoration:underline}
.buy{left:953px;top:2094px;width:134px;height:50px;border:2px solid var(--white);border-radius:26px;color:var(--white);font-weight:700;font-size:15px;display:flex;align-items:center;justify-content:center}

/* footer */
.footer{left:0;top:2216px;width:1200px;height:363px;background:var(--footer)}
.fcol{top:2288px;color:var(--white)}
.fcol h4{font-size:16px;font-weight:500;margin-bottom:18px;letter-spacing:.2px}
.fcol ul{list-style:none;font-size:14px;line-height:26.6px}
.social li{display:flex;align-items:center;gap:13px;line-height:33.5px}
.social i{width:30px;height:30px;border-radius:50%;background:#333;display:flex;align-items:center;justify-content:center}
.divider{left:113px;top:2508px;width:974px;height:1px;background:#2e2e2e}
.copy{left:0;width:1200px;top:2537px;text-align:center;color:var(--white);font-size:14px}
</style>
</head>
<body>

<header class="site-header abs">
  <div class="brand abs">Lumora.tv</div>
  <nav class="nav abs">
    <a class="home" href="#">Home</a>
    <a class="about" href="#">About Us</a>
    <a class="search" href="#" aria-label="Search"><svg width="16" height="16" viewBox="0 0 16 16"><circle cx="6.5" cy="6.5" r="4.8" fill="none" stroke="#fff" stroke-width="2.2"/><path d="M10 10l4 4" stroke="#fff" stroke-width="2.4" stroke-linecap="round"/></svg></a>
    <a class="touch" href="#">Get In Touch</a>
    <a class="signin" href="#"><svg width="16" height="16" viewBox="0 0 16 16"><circle cx="8" cy="8" r="7" fill="none" stroke="#fff" stroke-width="1.5"/><circle cx="8" cy="6.3" r="2.4" fill="#fff"/><path d="M3.6 12.6c1.2-2 2.6-2.7 4.4-2.7s3.2.7 4.4 2.7" fill="#fff"/></svg>Sign in</a>
  </nav>
</header>

<section class="hero abs" role="img" aria-label="Misty haunted house and bare trees under a night sky"></section>
<div class="follow abs">Follow us</div>
<div class="follow-line abs"></div>
<div class="follow-icons abs"><span></span><span></span><span></span></div>
<h1 class="hero-title abs heading">Ghost Stories</h1>
<p class="hero-copy abs">Lorem ipsum dolor sit amet, consectetur adipiscing elit, sed do eiusmod tempor incididunt ut labore et dolore .</p>
<a class="watch btn-grad abs" href="#">WATCH NOW <svg width="16" height="16" viewBox="0 0 16 16"><circle cx="8" cy="8" r="7" fill="#fff"/><path d="M6.3 4.8l4.6 3.2-4.6 3.2z" fill="#3aa6b5"/></svg></a>

<article class="tile feature abs" role="img" aria-label="Footballer volleying a ball in a stadium">
  <div class="shade"></div>
  <span class="live">Live</span>
  <h2>Lorem ipsum dolor sit amet, consectetur adipiscing elit</h2>
  <div class="date"><svg width="14" height="14" viewBox="0 0 14 14"><rect x="1" y="2.5" width="12" height="10.5" fill="none" stroke="#fff" stroke-width="1.3"/><path d="M1 5.5h12M4 1v3M10 1v3" stroke="#fff" stroke-width="1.3"/></svg>March 31, 2020s</div>
</article>
<article class="tile t-movies abs" role="img" aria-label="Action movie scene in a stadium"><div class="shade"></div><h3>Movies</h3><p>Lorem ipsum dolor amet, adipiscing</p></article>
<article class="tile t-seasons abs" role="img" aria-label="Couple laughing on a sofa from a series"><div class="shade"></div><h3>Seasons</h3><p>Lorem ipsum dolor adipiscing</p></article>
<article class="tile t-news abs" role="img" aria-label="Commuters on a train platform"><div class="shade"></div><h3>News</h3><p>Lorem ipsum dolor amet, adipiscing</p></article>
<article class="tile t-kids abs" role="img" aria-label="Cartoon campfire under a full moon"><div class="shade"></div><h3>Kids</h3><p>Lorem ipsum dolor adipiscing</p></article>

<h2 class="promo-title abs heading">Watch Thousands of Shows and<br>Movies Anytime, Anywhere</h2>
<p class="promo-copy abs">Lorem ipsum dolor sit amet, consectetur adipiscing elit, sed do eiusmod tempor incididunt ut labore et dolore magna aliqua. enim ad minim veniam,</p>
<a class="trial btn-grad abs" href="#">START YOUR FREE TRIAL</a>
<div class="phone phone-left abs"><div class="notch"></div><div class="phone-brand">Lumora.tv</div><div class="phone-login">Login</div></div>
<div class="phone phone-right abs" role="img" aria-label="Women jogging outdoors at sunset on a phone screen"><div class="notch"></div><div class="phone-caption">Lorem ipsum dolor amet,<br>consectetur</div></div>

<section class="contact abs"></section>
<h2 class="contact-title abs heading">Contact us</h2>
<p class="contact-copy abs">Lorem ipsum dolor sit amet, consectetur adipiscing elit, sed do eiusmod tempor incididunt ut labore et Ut enim</p>
<div class="field f-name abs"><svg width="14" height="14" viewBox="0 0 14 14"><rect x="1" y="3" width="9" height="9.5" fill="none" stroke="#555" stroke-width="1.3"/><path d="M6 8l6-6" stroke="#555" stroke-width="1.6"/></svg>Name</div>
<div class="field f-phone abs"><svg width="13" height="13" viewBox="0 0 13 13"><path d="M2 1l3 2.5-1.2 1.8c.9 1.7 2.2 3 3.9 3.9L9.5 8 12 11l-1.7 1.5C5.5 12 1 7.5.5 2.7z" fill="#555"/></svg>Phone</div>
<div class="field f-email abs"><svg width="15" height="12" viewBox="0 0 15 12"><rect x="0.5" y="1" width="14" height="10" fill="#555"/><path d="M1 1.5l6.5 5 6.5-5" stroke="#fff" stroke-width="1.2" fill="none"/></svg>Email</div>
<div class="field f-msg abs"><svg width="15" height="13" viewBox="0 0 15 13"><ellipse cx="7.5" cy="5.5" rx="7" ry="5" fill="#555"/><path d="M3 9l-1.5 3.5L6 10z" fill="#555"/></svg>Message</div>
<a class="submit btn-grad abs" href="#">SUBMIT</a>

<section class="bundle abs"></section>
<div class="partners abs"><span>Lumora.tv</span><span>Mirathon+</span><span>Sportiva+</span></div>
<div class="bundle-kicker abs">BUNDLE AND SAVE OVER 25%</div>
<div class="bundle-line abs">Get Lumora, Mirathon+, and Sportiva+ for $12.99/month.</div>
<a class="bundle-more abs" href="#">MORE DETAILS</a>
<a class="buy abs" href="#">BUY NOW</a>

<footer class="footer abs"></footer>
<div class="fcol abs" style="left:113px"><h4>BROWSE</h4><ul><li>Streaming Library</li><li>Live TV</li><li>Live News</li><li>Live Sports</li><li>TV Shows</li><li>Movies</li></ul></div>
<div class="fcol abs" style="left:250px"><h4>&nbsp;</h4><ul><li>Originals</li><li>Networks</li><li>Kids</li><li>Arc on Brindo</li><li>Halo Box</li><li>Cinevault</li></ul></div>
<div class="fcol abs" style="left:396px"><h4>HELP</h4><ul><li>Account &amp; Billing</li><li>Plans &amp; Pricing</li><li>Supported Devices</li><li>Accessibility</li></ul></div>
<div class="fcol abs" style="left:591px"><h4>ABOUT US</h4><ul><li>Press</li><li>Jobs</li><li>Contact</li><li>FAQ</li></ul></div>
<div class="fcol abs" style="left:751px"><h4>INFORMATION</h4><ul><li>Terms &amp; Conditions</li><li>Privacy Policy</li><li>Disclaimer</li><li>Site Map</li><li>Contact Us</li></ul></div>
<div class="fcol abs" style="left:952px"><h4>FOLLOW US</h4><ul class="social">
  <li><i><svg width="10" height="10" viewBox="0 0 10 10"><path d="M2 8l6-6M4 2h4v4" stroke="#fff" stroke-width="1.5" fill="none"/></svg></i>Pagebook</li>
  <li><i><svg width="10" height="10" viewBox="0 0 10 10"><path d="M2 8l6-6M4 2h4v4" stroke="#fff" stroke-width="1.5" fill="none"/></svg></i>Chirper</li>
  <li><i><svg width="10" height="10" viewBox="0 0 10 10"><path d="M2 8l6-6M4 2h4v4" stroke="#fff" stroke-width="1.5" fill="none"/></svg></i>Orbit Plus</li>
  <li><i><svg width="10" height="10" viewBox="0 0 10 10"><path d="M2 8l6-6M4 2h4v4" stroke="#fff" stroke-width="1.5" fill="none"/></svg></i>Linkwork</li>
</ul></div>
<div class="divider abs"></div>
<p class="copy abs">Copyrights © Lumora Tv 2020 | Allrights Reserved</p>

</body>
</html>
```